Business Card Design

We are a General Practice - Family medicine
We also have Allied Health professionals working within our team

Industry/Entity Type

Business

Contact Information for Business Card

Front of the card to display:

BRAMBLEWICK MEDICAL
PHONE 6348 2917

5/41 Fennimore Parade
Launceston Tasmania 7284

Back of the card to display:

My Appointments
Date:
Time:
With:

Please remember to phone us on 6348 2917 to cancel your appointment if you can't keep it.
A fee applied to missed appointments

```html
<!DOCTYPE html>
<html lang="en">
<head>
<meta charset="utf-8">
<title>Bramblewick Medical – Appointment Card</title>
<link rel="stylesheet" href="https://fonts.googleapis.com/css2?family=Open+Sans:ital,wght@0,400;0,700;1,400&display=swap">
<style>
  :root {
    --page-bg: #ebebeb;
    --card-bg: #ffffff;
    --brand-blue: #3fa9dc;
    --brand-green: #9cc43c;
    --leaf-green: rgba(160, 200, 70, 0.55);
    --leaf-blue: rgba(80, 170, 225, 0.5);
    --text-grey: #5f6368;
    --rule-grey: #6a6a6a;
  }
  * { box-sizing: border-box; margin: 0; padding: 0; }
  html, body {
    width: 955px;
    height: 1200px;
    overflow: hidden;
    background: var(--page-bg);
    font-family: "Open Sans", Arial, sans-serif;
    color: var(--text-grey);
  }
  .sheet { position: relative; width: 955px; height: 1200px; }

  .card {
    position: absolute;
    left: 103px;
    width: 755px;
    height: 461px;
    background: var(--card-bg);
    border-radius: 27px;
    overflow: hidden;
    box-shadow: 0 6px 14px rgba(0, 0, 0, 0.18);
  }
  .card--front { top: 93px; }
  .card--back { top: 627px; }

  /* soft brand-colour wash on the right edge */
  .brand-wash {
    position: absolute;
    top: 0;
    right: 0;
    height: 100%;
  }
  .card--front .brand-wash {
    width: 390px;
    background:
      radial-gradient(ellipse 62% 48% at 78% 28%, var(--leaf-green), rgba(255,255,255,0) 100%),
      radial-gradient(ellipse 70% 40% at 70% 78%, var(--leaf-blue), rgba(255,255,255,0) 100%);
  }
  .card--back .brand-wash {
    width: 215px;
    background:
      radial-gradient(ellipse 80% 45% at 90% 25%, var(--leaf-green), rgba(255,255,255,0) 100%),
      radial-gradient(ellipse 80% 35% at 90% 88%, var(--leaf-blue), rgba(255,255,255,0) 100%);
  }

  /* front */
  .brand-mark {
    position: absolute;
    left: 230px;
    top: 42px;
    width: 62px;
    height: 62px;
    border-radius: 50%;
    background: var(--brand-green);
  }
  .brand-name {
    position: absolute;
    left: 62px;
    top: 136px;
    font-size: 44px;
    font-weight: 400;
    color: var(--brand-blue);
    letter-spacing: -0.5px;
    white-space: nowrap;
  }
  .contact-row {
    position: absolute;
    left: 72px;
    display: flex;
    align-items: flex-start;
    gap: 8px;
  }
  .contact-row svg { flex: none; fill: var(--brand-blue); }
  .contact-row--phone { top: 268px; align-items: center; }
  .contact-row--phone .phone-number { font-size: 32px; line-height: 42px; }
  .contact-row--address { top: 338px; }
  .contact-row--address svg { margin-top: 9px; }
  .address { font-size: 26px; line-height: 37px; font-style: normal; }

  /* back */
  .appointments {
    position: absolute;
    left: 85px;
    top: 58px;
    width: 500px;
  }
  .appointments__title {
    font-size: 20px;
    font-weight: 700;
    color: var(--brand-blue);
    margin-bottom: 40px;
  }
  .field {
    display: flex;
    align-items: flex-end;
    font-size: 21px;
    height: 28px;
    margin-bottom: 40px;
  }
  .field__line {
    width: 356px;
    margin-left: 6px;
    border-bottom: 1.5px solid var(--rule-grey);
    height: 22px;
  }
  .note {
    font-size: 17.5px;
    font-style: italic;
    line-height: 24px;
    margin-top: -4px;
    width: 520px;
  }
  .note + .note { margin-top: 14px; }
</style>
</head>
<body>
<main class="sheet">

  <section class="card card--front" aria-label="Card front">
    <div class="brand-wash" role="img" aria-label="Soft green and blue brand colour wash"></div>
    <span class="brand-mark" aria-hidden="true"></span>
    <h1 class="brand-name">Bramblewick Medical</h1>

    <div class="contact-row contact-row--phone">
      <svg width="20" height="26" viewBox="0 0 20 26" aria-hidden="true">
        <path d="M5 1c1.2-.6 2.3 0 2.8 1.2l1.6 4c.4 1-.1 2-1 2.5l-1.5.8c.6 3.4 2 6.3 4.2 8.7l1.5-.6c1-.4 2 0 2.5.9l2.2 3.7c.6 1 .2 2.2-.8 2.7l-1.8 1C10 27 1 18 2.5 3z"/>
      </svg>
      <span class="phone-number">6348 2917</span>
    </div>

    <div class="contact-row contact-row--address">
      <svg width="18" height="34" viewBox="0 0 18 34" aria-hidden="true">
        <path d="M9 0a9 9 0 0 1 9 9c0 6-9 25-9 25S0 15 0 9a9 9 0 0 1 9-9zm0 4.5a4.5 4.5 0 1 0 0 9 4.5 4.5 0 0 0 0-9z"/>
      </svg>
      <address class="address">5/41 Fennimore Parade<br>Launceston Tasmania 7284</address>
    </div>
  </section>

  <section class="card card--back" aria-label="Card back">
    <div class="brand-wash" role="img" aria-label="Soft green and blue brand colour wash"></div>
    <div class="appointments">
      <h2 class="appointments__title">My appointments:</h2>
      <div class="field"><span>Date</span><span class="field__line"></span></div>
      <div class="field"><span>Time</span><span class="field__line"></span></div>
      <div class="field"><span>With</span><span class="field__line"></span></div>
      <p class="note">Please remember to phone us on 6348 2917 to cancel your appointment if you can't keep it.</p>
      <p class="note">A fee applied to missed appointments.</p>
    </div>
  </section>

</main>
</body>
</html>
```